Bravlo Official Introduction Powerpoint presentation

We are into business of Co working/ Ready to move in 100% customised plug and play office space company. Having large multinational like Tripvant, Ledgerwise, KLT etc as our customer using spaces .Need to get official PPT design for digital and print media. This should contain our product and services, locations, existing clients, testimonials, videos etc. The presentation has to be sent at the time of introduction of brand to potential customer so it has to cover all aspects in result leaving impact on the viewer where he should get inclined to do business with us.

Target Market(s)

Large multi national global organisations

Colors

Designer to choose colors to be used in the design.

Requirements
Must have
• Tag line : Kickstart your Way
• Crisp information, impactful images, testimonials, Design should speak luxury and class like a luxury 5 star hotel brand. We will provide photos of actual sites seperately. Use below link for photos of current t offices
• https://files.quorvane.com/share/7Rk2LmPq9XzT4vBn8WcYh3JdFs6Ga1-Ue?view=open
• Please take reference for content from this file
• https://pages.quorvane.com/doc/d/583mtwR-aZ7yKp2QxLcVb9NhEg4FjDu6Ws1TqHiO/view?mode=open
Nice to have
• Any new impactful thing, actual site pictures
• Use below link for photos of current t offices
Should not have
• Link to content: https://pages.quorvane.com/doc/d/583mtwR-aZ7yKp2QxLcVb9NhEg4FjDu6Ws1TqHiO/view?mode=open
• Images: This folder has all images related Bravlo relevant to the presentation: https://files.quorvane.com/share/4Mbqe9JrT2VzHk8NcLp3Wy5Gd-0XsFa1?view=open

```html
<!DOCTYPE html>
<html lang="en">
<head>
<meta charset="UTF-8">
<title>Layers of Service</title>
<link rel="stylesheet" href="https://fonts.googleapis.com/css2?family=Fira+Sans:wght@300;600;700&display=swap">
<style>
  :root {
    --brand-red: #ee2e3a;
    --ink: #1a1a1a;
    --paper: #ffffff;
  }
  html, body {
    margin: 0;
    padding: 0;
    overflow: hidden;
    background: var(--paper);
  }
  .slide {
    position: relative;
    width: 1200px;
    height: 675px;
    background: var(--paper);
    overflow: hidden;
    font-family: "Fira Sans", Arial, sans-serif;
  }
  .slide-title {
    position: absolute;
    left: 0;
    right: 0;
    top: 236px;
    margin: 0;
    text-align: center;
    font-size: 55px;
    font-weight: 600;
    letter-spacing: 2px;
    line-height: 1;
    color: var(--brand-red);
  }
  .title-rule {
    position: absolute;
    left: 473px;
    top: 305px;
    width: 255px;
    height: 3px;
    background: var(--brand-red);
  }
  .slide-lead {
    position: absolute;
    left: 0;
    right: 0;
    top: 346px;
    margin: 0;
    text-align: center;
    font-size: 26px;
    font-weight: 300;
    line-height: 34.5px;
    color: var(--ink);
  }
  .slide-lead strong {
    font-weight: 700;
  }
  .service-icon {
    position: absolute;
    left: 550px;
    top: 473px;
    width: 101px;
    height: 87px;
  }
</style>
</head>
<body>
  <main class="slide">
    <h1 class="slide-title">LAYERS OF SERVICE</h1>
    <div class="title-rule"></div>
    <p class="slide-lead">
      Every Layer is customized as per customer’s requirement.<br>
      You <strong>focus on your growth</strong>, we take care of the rest.
    </p>
    <svg class="service-icon" viewBox="0 0 116 100" fill="none" stroke="var(--brand-red)" stroke-width="2.8" stroke-linecap="round" stroke-linejoin="round" aria-hidden="true">
      <circle cx="5" cy="5" r="3.5"/>
      <polyline points="8.5,5 29,5 29,22"/>
      <circle cx="5" cy="50" r="3.5"/>
      <line x1="8.5" y1="50" x2="26" y2="50"/>
      <circle cx="5" cy="95" r="3.5"/>
      <polyline points="8.5,95 29,95 29,78"/>
      <circle cx="111" cy="5" r="3.5"/>
      <polyline points="107.5,5 87,5 87,22"/>
      <circle cx="111" cy="50" r="3.5"/>
      <line x1="107.5" y1="50" x2="90" y2="50"/>
      <circle cx="111" cy="95" r="3.5"/>
      <polyline points="107.5,95 87,95 87,78"/>
      <g transform="translate(58 50)">
        <polygon points="29.6,4.7 23.3,5.8 20.6,12.4 24.3,17.6 17.6,24.3 12.4,20.6 5.8,23.3 4.7,29.6 -4.7,29.6 -5.8,23.3 -12.4,20.6 -17.6,24.3 -24.3,17.6 -20.6,12.4 -23.3,5.8 -29.6,4.7 -29.6,-4.7 -23.3,-5.8 -20.6,-12.4 -24.3,-17.6 -17.6,-24.3 -12.4,-20.6 -5.8,-23.3 -4.7,-29.6 4.7,-29.6 5.8,-23.3 12.4,-20.6 17.6,-24.3 24.3,-17.6 20.6,-12.4 23.3,-5.8 29.6,-4.7"/>
        <circle r="16"/>
        <path d="M -6 -8 A 10 10 0 1 0 6 -8"/>
        <polygon points="4,0 2,3.5 -2,3.5 -4,0 -2,-3.5 2,-3.5"/>
      </g>
    </svg>
  </main>
</body>
</html>
```